Basic business card

use my newly created logo - and the phrases (Lower Cost of Test & Accelarated New Product Introduction) - and my new email domain / ID - use at conferences / tradeshows

Industry/Entity Type

semiconductor

Contact Information for Business Card

Lewis K Hardy, Owner, communicate via Logo - Lower COT - Cost of Test, Accelerated NPI - New Product Introduction, phone +1 480 555 0162, Chandler, Arizona, USA, lewis.hardy@vexalon-tsq.com

Font styles to use
Sans Serif

Requirements
Nice to have
• re-use my logo created via Artisan Hive last August (#5918206)

```html
<!DOCTYPE html>
<html lang="en">
<head>
<meta charset="utf-8">
<title>Vexalon-TSQ Business Card</title>
<link rel="stylesheet" href="https://fonts.googleapis.com/css2?family=Open+Sans:wght@400;600;700&display=swap">
<style>
  :root {
    --bg: #232323;
    --card: #151515;
    --slate: #4d5874;
    --emboss: #7a7a7a;
    --cyan: #41c3ec;
    --orange: #f6961f;
    --white: #f2f2f2;
  }
  * { margin: 0; padding: 0; box-sizing: border-box; }
  html, body {
    width: 1200px; height: 780px; overflow: hidden;
    background: var(--bg);
    font-family: "Open Sans", sans-serif;
  }
  .stage {
    width: 1200px; height: 780px;
    display: flex; align-items: center; justify-content: center; gap: 40px;
  }
  .card {
    position: relative; width: 520px; height: 300px;
    background: var(--card); overflow: hidden;
    box-shadow: 0 10px 30px rgba(0,0,0,.6);
  }
  .card-back { display: flex; align-items: center; justify-content: center; }
  .brand-mark {
    display: flex; align-items: center; gap: 14px;
    font-weight: 600; letter-spacing: 2px; white-space: nowrap;
  }
  .brand-mark .dot { display: block; background: currentColor; }
  .card-back .brand-mark { color: var(--emboss); font-size: 44px; }
  .card-back .brand-mark .dot { width: 22px; height: 22px; }
  .card-front .brand-mark {
    position: absolute; left: 40px; top: 152px;
    color: var(--slate); font-size: 24px; gap: 9px;
  }
  .card-front .brand-mark .dot { width: 13px; height: 13px; }
  .divider {
    position: absolute; left: 296px; top: 56px;
    width: 1px; height: 150px; background: var(--cyan);
  }
  .contact { position: absolute; left: 312px; top: 34px; color: var(--white); }
  .person { font-size: 20px; font-weight: 700; line-height: 1.1; white-space: nowrap; }
  .person .first { color: var(--orange); }
  .person .last { color: var(--cyan); }
  .role { font-size: 11.5px; margin-top: 2px; }
  .lines { list-style: none; margin-top: 14px; font-size: 11.5px; }
  .lines li { display: flex; align-items: center; gap: 7px; line-height: 18px; white-space: nowrap; }
  .lines svg { width: 11px; height: 11px; fill: var(--cyan); flex: none; }
  .address { margin-top: 12px; font-size: 11.5px; line-height: 17px; }
  .wave { position: absolute; left: 0; top: 0; width: 520px; height: 300px; }
</style>
</head>
<body>
<main class="stage">
  <section class="card card-back">
    <div class="brand-mark"><span class="dot"></span>VEXALON-TSQ</div>
  </section>

  <section class="card card-front">
    <div class="brand-mark"><span class="dot"></span>VEXALON-TSQ</div>
    <div class="divider"></div>
    <div class="contact">
      <p class="person"><span class="first">Lewis K</span> <span class="last">Hardy</span></p>
      <p class="role">Owner</p>
      <ul class="lines">
        <li><svg viewBox="0 0 12 12"><path d="M2 1h3l1 3-2 1c1 2 2 3 3 3l1-2 3 1v3c-6 1-10-3-9-9z"/></svg>+1 480 555 0162</li>
        <li><svg viewBox="0 0 12 12"><path d="M0 2h12v8H0z"/><path d="M1 3l5 4 5-4" fill="none" stroke="#151515" stroke-width="1.2"/></svg>lewis.hardy@vexalon-tsq.com</li>
        <li><svg viewBox="0 0 12 12"><circle cx="6" cy="6" r="5.5"/><path d="M6 .5v11M.5 6h11" stroke="#151515" stroke-width="1"/></svg>www.vexalon-tsq.com</li>
      </ul>
      <p class="address">Chandler, Arizona<br>USA</p>
    </div>
    <svg class="wave" viewBox="0 0 520 300" aria-hidden="true">
      <path d="M0 288 C80 250 200 242 310 234 S470 214 520 196 L520 300 L0 300Z" fill="var(--cyan)"/>
      <path d="M0 296 C80 258 200 249 310 241 S470 222 520 204 L520 300 L0 300Z" fill="var(--card)"/>
      <path d="M10 300 C90 264 200 256 310 248 S470 230 520 212 L520 300Z" fill="var(--orange)"/>
    </svg>
  </section>
</main>
</body>
</html>
```